Printing company needs stellar web site!

We need a website for a printing company based in Atlanta, Georgia, USA. Our company is 26 years old and just this year did a logo and branding refresh. Now we need our website to be refreshed as well.

Please see the attached source files for our new logo and stationary design.

Industry/Entity Type

Printing

```html
<!DOCTYPE html>
<html lang="en">
<head>
<meta charset="utf-8">
<title>Inkwell Printing</title>
<link href="https://fonts.googleapis.com/css2?family=PT+Sans:wght@400;700&family=Exo+2:wght@400;500&family=Arimo:wght@400;700&display=swap" rel="stylesheet">
<style>
:root{
  --page:#f7f7f7;
  --brand:#0e5fa8;
  --brand-dark:#0a3f78;
  --hero-top:#0760b0;
  --hero-bottom:#084d93;
  --accent:#ffd200;
  --ink:#2b2b2b;
  --muted:#555;
  --line:#d8d8d8;
  --sky:#2f9ff0;
  --price:#9b3b9b;
  --btn-top:#f5b21a;
  --btn-bottom:#d78a00;
  --footer:#0b5294;
}
*{box-sizing:border-box;margin:0;padding:0}
html,body{width:1119px;height:1200px;overflow:hidden;background:var(--page);font-family:"PT Sans",sans-serif;color:var(--ink)}
.page{position:relative;width:1119px;height:1200px}

.header{position:absolute;left:0;top:0;width:100%;height:105px;background:#f8f8f8}
.brand{position:absolute;left:91px;top:28px}
.brand-name{display:flex;align-items:center;gap:10px;font-family:"Exo 2",sans-serif;font-weight:500;font-size:42px;line-height:42px;color:var(--brand);letter-spacing:1px}
.brand-dot{width:38px;height:38px;border-radius:50%;background:var(--brand)}
.brand-tag{margin:4px 0 0 58px;font-family:"Arimo",sans-serif;font-size:10px;color:var(--brand);letter-spacing:-.2px}
.search{position:absolute;left:711px;top:37px;width:288px;height:34px;border:1px solid #dcdcdc;background:#f1f1f1;display:flex}
.search-field{flex:1;padding:8px 13px;font-size:14px;color:#888}
.search-btn{width:70px;margin:2px;background:var(--brand);color:#fff;font-size:14px;font-weight:700;display:flex;align-items:center;justify-content:center;letter-spacing:.5px}

.nav-bar{position:absolute;left:0;top:105px;width:100%;height:11px;background:var(--brand)}
.nav{position:absolute;left:0;top:116px;width:100%;height:42px;background:linear-gradient(#f6f6f6,#d9d9d9);display:flex;padding-left:94px;font-size:14px;font-weight:700;letter-spacing:.3px}
.nav-item{height:100%;display:flex;align-items:center;justify-content:center;border-right:1px solid #c5c5c5;color:#1c1c1c}
.nav-item:last-child{border-right:none}

.hero{position:absolute;left:0;top:158px;width:100%;height:313px;background:radial-gradient(ellipse at 52% 40%,#1288d8 0%,var(--hero-top) 40%,var(--hero-bottom) 100%)}
.hero-title{position:absolute;top:62px;width:100%;text-align:center;font-family:"Arimo",sans-serif;font-size:50px;color:#fff;word-spacing:10px;letter-spacing:1px}
.hero-tag{position:absolute;top:146px;width:100%;text-align:center;font-family:"Arimo",sans-serif;font-weight:700;font-size:17px;color:var(--accent);word-spacing:3px}

.service{position:absolute;top:392px;text-align:center}
.service-art{height:186px;border-radius:6px}
.service-label{margin-top:12px;font-size:27px;font-weight:700;line-height:24px;color:#333}

.panel-head{position:absolute;top:701px;height:49px;border-radius:8px 8px 0 0;display:flex;align-items:center;font-family:"Exo 2",sans-serif;font-size:25px;color:#fff}
.panel-head::after{content:"";position:absolute;inset:3px;border:1px dashed rgba(255,255,255,.7);border-radius:6px 6px 0 0;pointer-events:none}
.cat-head{left:94px;width:249px;background:linear-gradient(#1b67c8,#0a3b9a);padding-left:23px}
.feat-head{left:367px;width:647px;background:linear-gradient(#3aaaf5,#1e8fe6);padding-left:31px}
.arrows{position:absolute;right:7px;bottom:0;display:flex;gap:2px}
.arrow{width:20px;height:22px;display:flex;align-items:center;justify-content:center}
.arrow.prev{background:#1a1a1a}
.arrow.next{background:#1a8a1a}

.categories{position:absolute;left:94px;top:750px;width:249px;height:328px;background:linear-gradient(#fff,#f1f1f1);border-radius:0 0 8px 8px;box-shadow:0 0 3px rgba(0,0,0,.2)}
.cat{display:flex;align-items:center;height:38px;border-top:1px solid var(--line);padding-left:13px;font-size:18px;color:#333}
.cat-first{border-top:none;display:block;height:97px;padding-top:12px}
.cat-row{display:flex;align-items:center}
.bullet{width:14px;height:14px;border-radius:50%;background:#e8e8e8;border:1px solid #c9c9c9;margin-right:12px;display:flex;align-items:center;justify-content:center}
.sub{list-style:none;margin:2px 0 0 34px;font-size:12.5px;color:#444;line-height:18.5px}
.sub li::before{content:"";display:inline-block;border-left:4px solid #666;border-top:3.5px solid transparent;border-bottom:3.5px solid transparent;margin-right:6px}

.card{position:absolute;top:771px;width:201px;height:307px;border:1px dashed #9a9a9a;border-radius:6px;background:linear-gradient(#f0f0f0,#e4e4e4)}
.card-title{padding:10px 0 0 12px;font-family:"Exo 2",sans-serif;font-size:19px;color:#333;white-space:nowrap}
.card-sub{padding-left:12px;font-size:12px;color:#555}
.card-art{position:absolute;left:11px;top:58px;width:177px;height:168px;background:#fff;border:1px solid #ddd;display:flex;align-items:center;justify-content:center}
.card-art div{width:120px;height:120px;border-radius:8px}
.price{position:absolute;top:235px;width:100%;text-align:center;font-size:21px;color:var(--price)}
.buy{position:absolute;top:268px;left:50%;transform:translateX(-50%);width:81px;height:27px;background:linear-gradient(var(--btn-top),var(--btn-bottom));border:1px solid #a86a00;color:#fff;font-size:15px;font-weight:700;display:flex;align-items:center;justify-content:center}

.footer{position:absolute;left:0;top:1123px;width:100%;height:77px;background:var(--footer);font-family:"Arimo",sans-serif;color:#fff}
.footer-links{position:absolute;left:103px;top:18px;font-size:13px;word-spacing:1px}
.footer-links span{margin:0 10px}
.copyright{position:absolute;left:103px;top:42px;font-size:13px}
.footer-brand{position:absolute;left:749px;top:19px}
.footer-brand .brand-name{font-size:31px;line-height:31px;color:#dde6ef;gap:8px}
.footer-brand .brand-dot{width:30px;height:30px;background:#dde6ef}
.footer-brand .brand-tag{font-size:8px;margin:2px 0 0 46px;color:#dde6ef}
</style>
</head>
<body>
<div class="page">

  <header class="header">
    <div class="brand">
      <div class="brand-name"><span class="brand-dot"></span>INKWELL</div>
      <div class="brand-tag">OUTSTANDING SERVICE • QUALITY PRODUCT • COMPETITIVE PRICING.</div>
    </div>
    <div class="search">
      <div class="search-field">Search Keywords</div>
      <div class="search-btn">SEARCH</div>
    </div>
  </header>

  <div class="nav-bar"></div>
  <nav class="nav">
    <div class="nav-item" style="width:189px">CORPORATE IDENTITY</div>
    <div class="nav-item" style="width:131px">NOTEPAD</div>
    <div class="nav-item" style="width:131px">POSTER</div>
    <div class="nav-item" style="width:232px">PRESENTATION FOLDER</div>
    <div class="nav-item" style="width:230px">PROMOTIONAL PRODUCTS</div>
  </nav>

  <section class="hero">
    <h1 class="hero-title">WHAT CAN I PRINT DESIGN</h1>
    <p class="hero-tag">OUTSTANDING SERVICE &nbsp;* &nbsp;QUALITY PRODUCT &nbsp;* &nbsp;COMPETITIVE PRICING</p>
  </section>

  <div class="service" style="left:79px;width:191px">
    <div class="service-art" role="img" aria-label="Large-format printer producing a sunflower poster" style="background:linear-gradient(#c9ccd0,#f1f1ee 30%,#f6e07a 55%,#f2f2f2)"></div>
    <div class="service-label">Posters</div>
  </div>
  <div class="service" style="left:317px;width:258px">
    <div class="service-art" role="img" aria-label="Open presentation folder with handwritten notes and a pen" style="background:linear-gradient(135deg,#e6e6e6,#f7f7f7 50%,#e2b8df 75%,#8fd3ee)"></div>
    <div class="service-label">Presentation<br>Folders</div>
  </div>
  <div class="service" style="left:597px;width:187px">
    <div class="service-art" role="img" aria-label="Letterhead sheet tucked into an envelope" style="background:linear-gradient(160deg,#e0e0e0,#fafafa 50%,#f3e1a8 80%,#b9e4f2)"></div>
    <div class="service-label">Letterheads &amp;<br>Envelopes</div>
  </div>
  <div class="service" style="left:816px;width:247px">
    <div class="service-art" role="img" aria-label="Colour registration sticker and yellow shopping basket" style="background:linear-gradient(135deg,#e9e9e9,#f5f5f5 40%,#f7d21e 75%,#f0b400)"></div>
    <div class="service-label">Stickers</div>
  </div>

  <div class="panel-head cat-head">All Categories</div>
  <aside class="categories">
    <div class="cat cat-first">
      <div class="cat-row"><span class="bullet"><svg width="6" height="5"><path d="M0 0h6L3 5z" fill="#9b3b9b"/></svg></span>Poster</div>
      <ul class="sub"><li>Boys Tees &amp; Shirts</li><li>Skirts &amp; Frocks</li><li>Girls Tops</li></ul>
    </div>
    <div class="cat"><span class="bullet"><svg width="5" height="6"><path d="M0 0v6l5-3z" fill="#9b3b9b"/></svg></span>Presentation</div>
    <div class="cat"><span class="bullet"><svg width="5" height="6"><path d="M0 0v6l5-3z" fill="#9b3b9b"/></svg></span>Letterheads &amp; Envelopes</div>
    <div class="cat"><span class="bullet"><svg width="5" height="6"><path d="M0 0v6l5-3z" fill="#9b3b9b"/></svg></span>Stickers</div>
    <div class="cat"><span class="bullet"><svg width="5" height="6"><path d="M0 0v6l5-3z" fill="#9b3b9b"/></svg></span>Products</div>
    <div class="cat"><span class="bullet"><svg width="5" height="6"><path d="M0 0v6l5-3z" fill="#9b3b9b"/></svg></span>Quality</div>
    <div class="cat"><span class="bullet"><svg width="5" height="6"><path d="M0 0v6l5-3z" fill="#9b3b9b"/></svg></span>Letterhead</div>
  </aside>

  <div class="panel-head feat-head">Featured Products
    <div class="arrows">
      <div class="arrow prev"><svg width="6" height="10"><path d="M5 1L1 5l4 4" stroke="#fff" stroke-width="1.5" fill="none"/></svg></div>
      <div class="arrow next"><svg width="6" height="10"><path d="M1 1l4 4-4 4" stroke="#fff" stroke-width="1.5" fill="none"/></svg></div>
    </div>
  </div>

  <article class="card" style="left:368px">
    <div class="card-title">Poster</div>
    <div class="card-sub">Cat nap bags for baby</div>
    <div class="card-art"><div role="img" aria-label="Printer with sunflower poster" style="background:linear-gradient(#c9ccd0,#f6e07a 55%,#f2f2f2)"></div></div>
    <div class="price">$ 50.20</div>
    <div class="buy">Buy Now</div>
  </article>
  <article class="card" style="left:597px">
    <div class="card-title">Letterhead &amp; Envelop</div>
    <div class="card-sub">Cat nap bags for baby</div>
    <div class="card-art"><div role="img" aria-label="Printed brochure with colour swatches" style="background:linear-gradient(135deg,#f3d23a,#f4f4f4 45%,#d6a2d8 75%,#79c8ee)"></div></div>
    <div class="price">$ 50.20</div>
    <div class="buy">Buy Now</div>
  </article>
  <article class="card" style="left:823px">
    <div class="card-title">Note Pads</div>
    <div class="card-sub">Cat nap bags for baby</div>
    <div class="card-art"><div role="img" aria-label="Clipboard note pad with checklist and pen" style="background:linear-gradient(135deg,#4a4a4a,#e8e8e8 30%,#f6f6f6 65%,#8fd3ee)"></div></div>
    <div class="price">$ 50.20</div>
    <div class="buy">Buy Now</div>
  </article>

  <footer class="footer">
    <div class="footer-links">Corporate Identity<span>|</span>Notepad<span>|</span>Poster<span>|</span>Presentation Folder<span>|</span>Promotional Products</div>
    <div class="copyright">© 2014 INKWELL. All Rights Reserved.</div>
    <div class="footer-brand">
      <div class="brand-name"><span class="brand-dot"></span>INKWELL</div>
      <div class="brand-tag">OUTSTANDING SERVICE • QUALITY PRODUCT • COMPETITIVE PRICING.</div>
    </div>
  </footer>

</div>
</body>
</html>
```